Vacation giveaway landing page design

We are giving away a holiday/vacation to Rome and we need a landing page designed that will entice people to enter their email address for a chance to win!

Full brief, examples and everything else can be found in this document: https://files.quorvanshare.net/page/7-tmzrwpQY4vxkaLn8sbgeXu2fcTo5kWdn3jhpyuBc29m/open?mode=viewing

Number of Pages Required

1 page

```html
<!DOCTYPE html>
<html lang="en">
<head>
<meta charset="utf-8">
<title>The Wish Weavers – Free Prize Draw</title>
<link rel="stylesheet" href="https://fonts.googleapis.com/css2?family=Oswald:wght@500;700&family=Open+Sans:wght@400;600&display=swap">
<style>
  :root {
    --teal: #2fb8ae;
    --teal-dark: #2c5a5c;
    --red: #f5373b;
    --white: #ffffff;
    --ink: #3a3a3a;
    --line: #d9d9d9;
    --footer: #f1f1f1;
  }
  * { box-sizing: border-box; margin: 0; padding: 0; }
  html, body { width: 1067px; height: 1200px; overflow: hidden; background: var(--white); }
  body { position: relative; font-family: "Open Sans", Arial, sans-serif; color: var(--ink); }

  .hero { position: absolute; left: 0; top: 0; width: 1067px; height: 730px; overflow: hidden; }
  .hero-backdrop {
    position: absolute; inset: 0;
    background: linear-gradient(180deg, #e2f0f6 0%, #b9ccd6 14%, #6d8796 30%, #3f5e70 46%, #2f5063 62%, #3c5d6f 78%, #56727f 100%);
  }
  .hero-curve { position: absolute; left: 0; top: 0; }

  .brand { position: absolute; top: 30px; left: 0; width: 1067px; display: flex; justify-content: center; align-items: center; gap: 12px; }
  .brand-dot { width: 46px; height: 46px; border-radius: 50%; border: 3px solid var(--teal-dark); }
  .brand-name { font-family: "Oswald", Arial, sans-serif; font-weight: 700; font-size: 34px; letter-spacing: 1px; color: var(--teal-dark); line-height: 1; }

  .hero-title { position: absolute; top: 170px; width: 100%; text-align: center; font-family: "Oswald", Arial, sans-serif; font-weight: 700; font-size: 56px; line-height: 1; color: var(--white); letter-spacing: 0.5px; }
  .hero-subtitle { position: absolute; top: 247px; width: 100%; text-align: center; font-family: "Oswald", Arial, sans-serif; font-weight: 700; font-size: 30px; line-height: 1; color: var(--white); }

  .signup { position: absolute; left: 254px; top: 298px; width: 562px; height: 57px; background: var(--white); border-radius: 29px; display: flex; align-items: center; padding-left: 26px; }
  .signup-icon { margin-right: 10px; }
  .signup-field { font-size: 15px; color: #555; letter-spacing: 0.3px; }
  .signup-button { position: absolute; right: 10px; top: 9px; width: 132px; height: 39px; border-radius: 20px; background: var(--red); color: var(--white); font-family: "Oswald", Arial, sans-serif; font-weight: 700; font-size: 17px; display: flex; align-items: center; justify-content: center; }

  .consent { position: absolute; top: 366px; left: 200px; width: 667px; text-align: center; font-size: 13.5px; line-height: 21px; color: var(--white); }

  .winners-heading { position: absolute; top: 427px; width: 100%; text-align: center; font-family: "Oswald", Arial, sans-serif; font-weight: 700; font-size: 22px; color: var(--white); }
  .winners-heading span { display: inline-block; width: 18px; height: 2px; background: var(--white); vertical-align: middle; margin: 0 6px; }

  .winner { position: absolute; display: flex; align-items: flex-start; }
  .winner-photo { width: 124px; height: 124px; border-radius: 50%; background: radial-gradient(circle at 45% 40%, #d9b4a2 0%, #b98e7d 45%, #5b4b47 100%); flex: none; }
  .winner-text { margin-left: 12px; color: var(--white); }
  .winner-name { font-family: "Oswald", Arial, sans-serif; font-weight: 500; font-size: 18px; line-height: 23px; }
  .winner-when { font-family: "Oswald", Arial, sans-serif; font-weight: 500; font-size: 16px; line-height: 22px; margin-bottom: 8px; }
  .winner-body { font-size: 12.5px; line-height: 19px; width: 240px; }
  .winner-link { font-size: 12.5px; line-height: 21px; }
  .winner-one { left: 147px; top: 478px; }
  .winner-one .winner-text { margin-top: 10px; }
  .winner-two { left: 550px; top: 470px; }

  .carousel-arrow { position: absolute; top: 522px; }

  .prizes-title { position: absolute; top: 745px; width: 100%; text-align: center; font-family: "Oswald", Arial, sans-serif; font-weight: 700; font-size: 38px; color: var(--teal); }

  .plan { position: absolute; top: 807px; width: 397px; height: 237px; background: var(--white); border: 1px solid var(--line); box-shadow: 0 1px 3px rgba(0,0,0,0.08); overflow: hidden; }
  .plan-premium { left: 139px; }
  .plan-basic { left: 560px; }
  .plan-title { position: absolute; left: 30px; top: 20px; font-family: "Oswald", Arial, sans-serif; font-weight: 700; font-size: 23px; color: var(--red); }
  .plan-features { position: absolute; left: 30px; top: 62px; list-style: none; }
  .plan-features li { display: flex; align-items: center; height: 25.5px; font-size: 12.5px; color: #444; letter-spacing: 0.2px; }
  .plan-features svg { margin-right: 8px; flex: none; }
  .plan-button { position: absolute; left: 26px; top: 174px; width: 134px; height: 40px; border-radius: 20px; background: var(--red); color: var(--white); font-family: "Oswald", Arial, sans-serif; font-weight: 700; font-size: 17px; display: flex; align-items: center; justify-content: center; }
  .price-ring { position: absolute; left: 258px; top: 108px; width: 290px; height: 290px; border-radius: 50%; background: var(--red); }
  .price-disc { position: absolute; left: 262px; top: 116px; width: 290px; height: 290px; border-radius: 50%; background: var(--teal); }
  .price { position: absolute; left: 276px; top: 152px; width: 120px; text-align: center; color: var(--white); font-family: "Oswald", Arial, sans-serif; font-weight: 700; }
  .price-amount { font-size: 36px; line-height: 40px; }
  .price-period { font-size: 16px; line-height: 20px; }

  .site-footer { position: absolute; left: 0; top: 1134px; width: 1067px; height: 66px; background: var(--footer); border-top: 1px solid #e2e2e2; text-align: center; padding-top: 21px; font-size: 13.5px; color: #222; }
</style>
</head>
<body>

<header class="hero">
  <div class="hero-backdrop" role="img" aria-label="Photo of a family running into the sea at the beach"></div>

  <div class="brand">
    <div class="brand-dot"></div>
    <div class="brand-name">THE WISH WEAVERS</div>
  </div>

  <h1 class="hero-title">THE WISH WEAVERS</h1>
  <h2 class="hero-subtitle">FREE ENTRY INTO A PRIZE DRAW</h2>

  <form class="signup">
    <svg class="signup-icon" width="17" height="13" viewBox="0 0 17 13" aria-hidden="true">
      <rect x="0" y="0" width="17" height="13" rx="1.5" fill="#2fb8ae"/>
      <path d="M1 1.5 L8.5 7 L16 1.5" fill="none" stroke="#fff" stroke-width="1.5"/>
    </svg>
    <span class="signup-field">EMAIL ADDRESS</span>
    <span class="signup-button">CLICK HERE</span>
  </form>

  <p class="consent">By entering your email address, you agree to receive updates about the competition and The Wish Weavers. You can review our competition terms and conditions here</p>

  <h3 class="winners-heading"><span></span>RECENT WINNERS<span></span></h3>

  <svg class="carousel-arrow" style="left:90px" width="22" height="42" viewBox="0 0 22 42" aria-hidden="true">
    <path d="M20 2 L2 21 L20 40" fill="none" stroke="#fff" stroke-width="2"/>
  </svg>
  <svg class="carousel-arrow" style="left:953px" width="22" height="42" viewBox="0 0 22 42" aria-hidden="true">
    <path d="M2 2 L20 21 L2 40" fill="none" stroke="#fff" stroke-width="2"/>
  </svg>

  <article class="winner winner-one">
    <div class="winner-photo" role="img" aria-label="Portrait photo of this month's winner"></div>
    <div class="winner-text">
      <div class="winner-name">The Wish Weavers</div>
      <div class="winner-when">about a year ago</div>
      <p class="winner-body">We are very happy to announce that this month's winner is Harriet Dunmore!</p>
      <div class="winner-link">Learn More</div>
    </div>
  </article>

  <article class="winner winner-two">
    <div class="winner-photo" role="img" aria-label="Photo of the previous month's winner with a friend"></div>
    <div class="winner-text">
      <div class="winner-name">The Wish Weavers</div>
      <div class="winner-when">about a year ago</div>
      <p class="winner-body">Another month, another winner! Congratulations to Marisol Ventura!</p>
      <div class="winner-link">Learn More</div>
    </div>
  </article>

  <svg class="hero-curve" width="1067" height="730" viewBox="0 0 1067 730" aria-hidden="true">
    <path d="M0 590 Q533.5 806 1067 590 L1067 730 L0 730 Z" fill="#fff"/>
    <path d="M0 603 Q533.5 831 1067 603" fill="none" stroke="#2fb8ae" stroke-width="4"/>
  </svg>
</header>

<h2 class="prizes-title">PRIZES</h2>

<section class="plan plan-premium">
  <h3 class="plan-title">15 ENTRIES &amp; WEEKLY DEALS</h3>
  <ul class="plan-features">
    <li><svg width="14" height="14" viewBox="0 0 14 14" aria-hidden="true"><circle cx="7" cy="7" r="6" fill="none" stroke="#f5373b" stroke-width="1.4"/><path d="M4 7.2 L6.2 9.3 L10 5" fill="none" stroke="#f5373b" stroke-width="1.4"/></svg>WEEKLY DEALS EMAIL (?)</li>
    <li><svg width="14" height="14" viewBox="0 0 14 14" aria-hidden="true"><circle cx="7" cy="7" r="6" fill="none" stroke="#f5373b" stroke-width="1.4"/><path d="M4 7.2 L6.2 9.3 L10 5" fill="none" stroke="#f5373b" stroke-width="1.4"/></svg>SAVE £100’S ON HOLIDAYS (?)</li>
    <li><svg width="14" height="14" viewBox="0 0 14 14" aria-hidden="true"><circle cx="7" cy="7" r="6" fill="none" stroke="#f5373b" stroke-width="1.4"/><path d="M4 7.2 L6.2 9.3 L10 5" fill="none" stroke="#f5373b" stroke-width="1.4"/></svg>MONTHLY MAGAZINE (?)</li>
    <li><svg width="14" height="14" viewBox="0 0 14 14" aria-hidden="true"><circle cx="7" cy="7" r="6" fill="none" stroke="#f5373b" stroke-width="1.4"/><path d="M4 7.2 L6.2 9.3 L10 5" fill="none" stroke="#f5373b" stroke-width="1.4"/></svg>15 ENTRIES EVERY MONTH</li>
  </ul>
  <span class="plan-button">CHECK OUT</span>
  <div class="price-ring"></div>
  <div class="price-disc"></div>
  <div class="price"><div class="price-amount">£4.99</div><div class="price-period">PER MONTH</div></div>
</section>

<section class="plan plan-basic">
  <h3 class="plan-title">1 ENTRY</h3>
  <ul class="plan-features">
    <li><svg width="14" height="14" viewBox="0 0 14 14" aria-hidden="true"><rect x="1" y="1" width="12" height="12" fill="none" stroke="#f5373b" stroke-width="1.4"/><path d="M4.5 4.5 L9.5 9.5 M9.5 4.5 L4.5 9.5" stroke="#f5373b" stroke-width="1.4"/></svg>WEEKLY DEALS EMAIL (?)</li>
    <li><svg width="14" height="14" viewBox="0 0 14 14" aria-hidden="true"><circle cx="7" cy="7" r="6" fill="none" stroke="#f5373b" stroke-width="1.4"/><path d="M4 7.2 L6.2 9.3 L10 5" fill="none" stroke="#f5373b" stroke-width="1.4"/></svg>SAVE £100’S ON HOLIDAYS (?)</li>
    <li><svg width="14" height="14" viewBox="0 0 14 14" aria-hidden="true"><circle cx="7" cy="7" r="6" fill="none" stroke="#f5373b" stroke-width="1.4"/><path d="M4 7.2 L6.2 9.3 L10 5" fill="none" stroke="#f5373b" stroke-width="1.4"/></svg>MONTHLY MAGAZINE (?)</li>
    <li><svg width="14" height="14" viewBox="0 0 14 14" aria-hidden="true"><circle cx="7" cy="7" r="6" fill="none" stroke="#f5373b" stroke-width="1.4"/><path d="M4 7.2 L6.2 9.3 L10 5" fill="none" stroke="#f5373b" stroke-width="1.4"/></svg>1 ENTRY EVERY MONTH</li>
  </ul>
  <span class="plan-button">CHECK OUT</span>
  <div class="price-ring"></div>
  <div class="price-disc"></div>
  <div class="price"><div class="price-amount">£2.99</div><div class="price-period">PER MONTH</div></div>
</section>

<footer class="site-footer">© 2019 Company Name&nbsp; All right reserved</footer>

</body>
</html>
```